MODELS AGENCY NEW YEAR 2026 CARD

A 10 cm x 21 cm horizontal New Year card for clients of our 2 models agencies, Brindel (kids) and Pavaduel (actors and adults) (logo in the jobs).

Side A of the card: creative mission:
-text: 2026
-text: Peace and Love
-Studio or movie set atmosphere
-tone of voice: optimistic, positive, colorful

Side B:
(name of 4 people of the agency:)
Solange, Anne-Sophie, Josiane & Paul-Henri,
(2 logos)
Brindel & PavaDuel
(Adres)
Rue des Tilleuls 74 b3 - 1060 Bruxelles - Belgique

Target Market(s)

Movie directors, photographers

Industry/Entity Type

Fashion, advertising & Movies

Requirements
Must have
• SEE TEXT IN BRIEFING

```html
<!DOCTYPE html>
<html lang="en">
<head>
<meta charset="utf-8">
<title>Pavaduel &amp; Brindel – New Year Card 2026</title>
<link rel="stylesheet" href="https://fonts.googleapis.com/css2?family=Barlow:wght@300;400;600&family=Big+Shoulders+Display:wght@200&family=Exo+2:wght@700&display=swap">
<style>
  :root {
    --sheet: #ffffff;
    --mat: #c5c6c8;
    --band: rgba(104, 94, 146, 0.85);
    --ink: #3b1d5a;
    --ink-soft: #6a5b80;
    --white: #ffffff;
    --frame-line: rgba(255, 255, 255, 0.9);
  }
  * { box-sizing: border-box; margin: 0; padding: 0; }
  html, body {
    width: 1153px; height: 1200px; overflow: hidden;
    background: var(--sheet);
  }
  .mat {
    position: absolute; left: 15px; top: 15px;
    width: 1122px; height: 1169px;
    background: var(--mat);
  }
  .card {
    position: absolute; left: 61px; width: 1027px; height: 489px;
    overflow: hidden;
  }
  .side-a { top: 86px; }
  .side-b { top: 638px; background: var(--sheet); }

  .studio-photo {
    position: absolute; inset: 0;
    background:
      radial-gradient(circle at 30% 8%, #f7d9a4 0, rgba(247,217,164,0) 12%),
      radial-gradient(circle at 48% 12%, #fbeed4 0, rgba(251,238,212,0) 10%),
      linear-gradient(100deg, #d9d3cb 0%, #f1efec 25%, #e7e1d8 45%, #ecebea 60%, #cfccc9 80%, #a8a4a2 100%);
  }
  .band {
    position: absolute; left: 0; right: 0; top: 150px; height: 189px;
    background: var(--band);
  }
  .frame {
    position: absolute; left: 24px; top: 24px; width: 978px; height: 441px;
    border: 1px solid var(--frame-line);
  }
  .site-url {
    position: absolute; left: 21px; top: 19px;
    font: 400 13px/1 "Barlow", sans-serif;
    letter-spacing: 0.5px;
    color: #5d5670;
  }
  .year {
    position: absolute; left: 104px; top: 178px;
    font: 700 142px/1 "Exo 2", sans-serif;
    color: var(--white);
    letter-spacing: 2px;
  }
  .motto {
    position: absolute; left: 520px; top: 230px;
    font: 200 58px/1 "Big Shoulders Display", sans-serif;
    color: var(--white);
    letter-spacing: 18px;
    text-transform: uppercase;
  }

  .team {
    position: absolute; left: 0; right: 0; top: 100px;
    text-align: center;
    font: 300 31px/1.2 "Barlow", sans-serif;
    color: var(--ink);
  }
  .agency {
    position: absolute; top: 220px; width: 300px;
    text-align: center; color: var(--ink);
  }
  .agency-adults { left: 179px; }
  .agency-kids { left: 557px; }
  .agency-name {
    display: flex; align-items: center; justify-content: center; gap: 10px;
    font: 600 44px/1 "Barlow", sans-serif;
    letter-spacing: 2px;
  }
  .agency-dot {
    width: 14px; height: 14px; border-radius: 50%;
    background: var(--ink);
  }
  .agency-tagline {
    margin-top: 14px;
    font: 400 13px/1 "Barlow", sans-serif;
    letter-spacing: 2.4px;
    text-transform: uppercase;
  }
  .agency-since {
    margin-top: 60px;
    font: 400 10px/1 "Barlow", sans-serif;
    letter-spacing: 0.5px;
    color: var(--ink-soft);
  }
  .address {
    position: absolute; left: 0; right: 0; top: 444px;
    text-align: center;
    font: 300 21px/1 "Barlow", sans-serif;
    color: var(--ink);
  }
</style>
</head>
<body>
  <div class="mat"></div>

  <section class="card side-a">
    <div class="studio-photo" role="img" aria-label="Bright photo studio with spotlights, a young woman holding a tablet and a film crew behind cameras on tripods"></div>
    <div class="band"></div>
    <div class="frame"></div>
    <p class="site-url">www.pavaduel.be</p>
    <h1 class="year">2026</h1>
    <p class="motto">Peace and Love</p>
  </section>

  <section class="card side-b">
    <p class="team">Solange, Anne-Sophie, Josiane &amp; Paul-Henri</p>

    <div class="agency agency-adults">
      <div class="agency-name"><span class="agency-dot"></span>PAVADUEL</div>
      <p class="agency-tagline">People, actors &amp; models agency</p>
      <p class="agency-since">– SINCE 2000 –</p>
    </div>

    <div class="agency agency-kids">
      <div class="agency-name"><span class="agency-dot"></span>BRINDEL</div>
      <p class="agency-tagline">Children models agency</p>
      <p class="agency-since">– SINCE 1982 –</p>
    </div>

    <p class="address">Rue des Tilleuls 74 b3 - 1060 Bruxelles - Belgique</p>
  </section>
</body>
</html>
```